Create a website in Wordpress for an interior design company

Create a website for our interior design company 'Roomora'

-Color preferences - Neutral and warm colors. Nothing too bright
-Aesthetic: Modern, Minimalist, Classic, Mature, Luxury
-Mission Statement: Transforming homes into personalized dream spaces through exceptional interior design, meticulous attention to detail, and a touch of the unexpected.
-Brand Values: innovation, creativity, passion and sustainability

Examples: https://www.lenamarchwoodinteriors.com.au/
https://www.tidecraftstudio.com/

About
Portfolio
Inquire page

```html
<!DOCTYPE html>
<html lang="en">
<head>
<meta charset="UTF-8">
<title>Roomora — Interior Design</title>
<link rel="stylesheet" href="https://fonts.googleapis.com/css2?family=Epilogue:wght@400;500;600;700&family=EB+Garamond:wght@400;500&display=swap">
<style>
  :root {
    --cream: #f5f2ec;
    --ink: #2b2b29;
    --slate: #aab5b6;
    --sage: #a0aa9e;
    --sage-btn: #9ea79a;
    --line: #8f9a9b;
    --white: #ffffff;
  }
  * { box-sizing: border-box; margin: 0; padding: 0; }
  html, body { width: 1200px; height: 3651px; overflow: hidden; }
  body { background: var(--cream); color: var(--ink); font-family: "EB Garamond", Georgia, serif; position: relative; }
  .abs { position: absolute; }
  .sans { font-family: "Epilogue", Arial, sans-serif; }
  .btn {
    position: absolute; display: flex; align-items: center; justify-content: center;
    border: 1.5px solid var(--ink); font-family: "Epilogue", Arial, sans-serif;
    font-weight: 600; font-size: 14px; letter-spacing: .3px; color: var(--ink); text-transform: uppercase;
  }
  .btn--filled { background: var(--sage-btn); }
  .photo { position: absolute; }

  /* header */
  .site-header { position: absolute; left: 0; top: 0; width: 1200px; height: 91px; }
  .brand { position: absolute; left: 110px; top: 26px; font-family: "Epilogue", Arial, sans-serif; font-weight: 700; font-size: 31px; letter-spacing: .5px; }
  .main-nav { position: absolute; left: 635px; top: 31px; display: flex; gap: 20px; font-size: 16px; }
  .main-nav .is-current { font-weight: 500; }

  /* hero */
  .hero { position: absolute; left: 0; top: 91px; width: 1200px; height: 471px; border-top: 1px solid var(--line); border-bottom: 1px solid var(--line); }
  .hero__panel { position: absolute; left: 602px; top: 0; width: 598px; height: 100%; background: var(--slate); border-left: 1px solid var(--line); }
  .hero__title { position: absolute; left: 67px; top: 78px; font-family: "Epilogue", Arial, sans-serif; font-weight: 500; font-size: 40px; line-height: 48px; white-space: nowrap; }
  .hero__text { position: absolute; left: 72px; top: 198px; font-family: "Epilogue", Arial, sans-serif; font-size: 20px; line-height: 30px; white-space: nowrap; }

  /* mission */
  .mission-label { left: 0; width: 1200px; top: 628px; text-align: center; font-size: 13px; font-weight: 600; letter-spacing: .5px; }
  .mission-text { left: 0; width: 1200px; top: 662px; text-align: center; font-family: "Epilogue", Arial, sans-serif; font-weight: 500; font-size: 40px; line-height: 48px; white-space: nowrap; }

  /* about */
  .section-title { font-family: "Epilogue", Arial, sans-serif; font-weight: 500; font-size: 40px; }
  .about-copy { left: 110px; top: 1640px; width: 470px; font-size: 16px; line-height: 28px; white-space: nowrap; }
  .about-copy p + p { margin-top: 7px; }

  /* inquiry */
  .inquiry { left: 110px; top: 2198px; width: 978px; height: 518px; border: 1px solid var(--line); background: var(--sage); }
  .inquiry__intro { position: absolute; left: 494px; top: 50px; width: 420px; font-size: 16px; line-height: 28px; }
  .field { position: absolute; left: 494px; width: 406px; height: 54px; background: var(--white); border: 1px solid #c9ccc6;
           font-family: "Epilogue", Arial, sans-serif; font-size: 15px; display: flex; align-items: center; padding-left: 26px; }
  .field svg { position: absolute; right: 24px; top: 23px; }

  /* portfolio */
  .portfolio-grid { left: 110px; top: 2898px; display: flex; gap: 14px; }
  .portfolio-grid div { width: 234px; height: 248px; }

  /* footer */
  .site-footer { position: absolute; left: 0; top: 3283px; width: 1200px; height: 368px; background: var(--slate); border-top: 1px solid var(--line); }
  .footer-brand { position: absolute; left: 0; width: 1200px; top: 40px; text-align: center; font-family: "Epilogue", Arial, sans-serif; font-weight: 700; font-size: 31px; }
  .footer-nav { position: absolute; left: 0; width: 1200px; top: 94px; display: flex; justify-content: center; gap: 23px; font-size: 18px; }
  .footer-rule { position: absolute; left: 110px; width: 978px; height: 1px; background: #939e9f; }
  .contact-item { position: absolute; top: 190px; font-size: 16px; line-height: 26px; white-space: nowrap; }
  .contact-item h4 { font-weight: 400; font-size: 16px; text-transform: uppercase; }
  .contact-icon { position: absolute; top: 194px; }
  .copyright { position: absolute; left: 0; width: 1200px; top: 325px; text-align: center; font-size: 12px; }
</style>
</head>
<body>

<header class="site-header">
  <div class="brand">ROOMORA</div>
  <nav class="main-nav">
    <span class="is-current">Home</span><span>About</span><span>Portfolio</span><span>Inquiry</span>
  </nav>
  <div class="btn btn--filled" style="left:934px;top:24px;width:154px;height:41px;">Get Started</div>
</header>

<section class="hero">
  <div class="photo" role="img" aria-label="Bright living room with curved cream sofas, round black coffee table and tall windows"
       style="left:0;top:0;width:602px;height:469px;background:linear-gradient(135deg,#d9d4cb 0%,#c8bfb2 45%,#8a7f72 75%,#3b3632 100%);"></div>
  <div class="hero__panel">
    <h1 class="hero__title">Elevate Your Space<br>with Timeless Design</h1>
    <p class="hero__text">From concept to completion, Roomora<br>creates elegant, functional interiors<br>that reflect your unique style and needs.</p>
    <div class="btn" style="left:72px;top:330px;width:154px;height:41px;">Get Started</div>
  </div>
</section>

<div class="abs mission-label sans">OUR MISSION</div>
<h2 class="abs mission-text">Transforming homes into personalized<br>dream spaces through exceptional interior<br>design, meticulous attention to detail, and<br>a touch of the unexpected.</h2>

<div class="photo" role="img" aria-label="Living room with cream sofa, terracotta cushions, abstract artwork and a black cone coffee table"
     style="left:0;top:917px;width:1200px;height:548px;border-top:1px solid var(--line);border-bottom:1px solid var(--line);background:linear-gradient(180deg,#e6e0d7 0%,#d8cfc3 50%,#b9aa98 80%,#8d7d6c 100%);"></div>

<h2 class="abs section-title" style="left:110px;top:1562px;">About Us</h2>
<div class="abs about-copy">
  <p>Lorem ipsum dolor sit amet, consectetur adipiscing elit, sed do eius<br>mod tempor incididunt ut labore et dolore magna aliqua. Quis ipsum<br>suspendisse ultrices gravida. Risus commodo viverra maecenas ac<br>cumsan lacus vel facilisis.</p>
  <p>Consectetur adipiscing elit, sed do eius mod tempor incididunt ut<br>labore et dolore magna aliqua. Quis ipsum suspendisse ultrices gravi<br>da. Risus commodo viverra maecenas ac cumsan lacus vel facilisis.</p>
</div>
<div class="btn btn--filled" style="left:112px;top:1887px;width:153px;height:41px;">Learn More</div>
<div class="photo" role="img" aria-label="Open-plan dining and living space with wooden table and leather sofa"
     style="left:612px;top:1675px;width:476px;height:314px;background:linear-gradient(160deg,#5e5a52 0%,#a49a8c 50%,#d5d1ca 100%);"></div>
<div class="photo" role="img" aria-label="Green paint swatches and fabric samples with a leafy branch"
     style="left:740px;top:1519px;width:352px;height:225px;border:4px solid var(--cream);background:linear-gradient(135deg,#8a8f84 0%,#6e8a5d 45%,#a9bb85 70%,#788a6e 100%);"></div>

<h2 class="abs section-title" style="left:0;width:1200px;text-align:center;top:2070px;">Let's Bring Your Vision to Life</h2>
<p class="abs" style="left:0;width:1200px;text-align:center;top:2132px;font-size:16px;">Have questions or ready to start your design journey? We'd love to hear from you!</p>

<section class="abs inquiry">
  <div class="photo" role="img" aria-label="Cosy sitting room with a green sofa, round wooden table and tall window"
       style="left:0;top:0;width:439px;height:516px;border-right:1px solid var(--line);background:linear-gradient(150deg,#d7cfc2 0%,#a8977f 45%,#6f6a45 75%,#4a3a2c 100%);"></div>
  <p class="inquiry__intro">Fill out the form below, and our team will be in touch soon to discuss your project.</p>
  <div class="field" style="top:131px;">Name</div>
  <div class="field" style="top:199px;">Mobile</div>
  <div class="field" style="top:269px;">Email</div>
  <div class="field" style="top:343px;">Select Interest
    <svg width="10" height="6" viewBox="0 0 10 6"><path d="M0 0h10L5 6z" fill="#2b2b29"/></svg>
  </div>
  <div class="btn" style="left:494px;top:432px;width:153px;height:41px;">Submit Noe</div>
</section>

<h2 class="abs section-title" style="left:0;width:1200px;text-align:center;top:2806px;">Our Portfolio</h2>
<div class="abs portfolio-grid">
  <div role="img" aria-label="Light living room with beige sofa and framed botanical prints" style="background:linear-gradient(180deg,#ebe8e3,#cfc4b4);"></div>
  <div role="img" aria-label="Dark kitchen with marble island and brass pendant lights" style="background:linear-gradient(180deg,#3c3f3e,#8b8378 60%,#d8cdbf);"></div>
  <div role="img" aria-label="Bathroom with freestanding tub under a slanted window" style="background:linear-gradient(180deg,#e9e8e4,#c9c2b5 55%,#a57a4f);"></div>
  <div role="img" aria-label="Living room with teal wall, grey sofa and woven pendant" style="background:linear-gradient(180deg,#7f9595,#b9b7ae 60%,#e2ddd4);"></div>
</div>
<div class="btn btn--filled" style="left:523px;top:3190px;width:153px;height:41px;">Explore More</div>

<footer class="site-footer">
  <div class="footer-brand">ROOMORA</div>
  <nav class="footer-nav"><span>Home</span><span>About</span><span>Portfolio</span><span>Inquiry</span><span>Contact</span></nav>
  <div class="footer-rule" style="top:151px;"></div>

  <svg class="contact-icon" style="left:113px;" width="18" height="22" viewBox="0 0 18 22" fill="none" stroke="#2b2b29" stroke-width="1.5"><path d="M9 21s7-7 7-12A7 7 0 0 0 2 9c0 5 7 12 7 12z"/><circle cx="9" cy="9" r="2.5"/></svg>
  <div class="contact-item" style="left:153px;"><h4>Address</h4>Roomora,<br>address comes here</div>

  <svg class="contact-icon" style="left:381px;top:197px;" width="22" height="16" viewBox="0 0 22 16" fill="none" stroke="#2b2b29" stroke-width="1.5"><rect x="1" y="1" width="20" height="14"/><path d="M1 1l10 8 10-8"/></svg>
  <div class="contact-item" style="left:418px;"><h4>Email</h4>info@roomora.com</div>

  <svg class="contact-icon" style="left:648px;" width="22" height="22" viewBox="0 0 24 24" fill="none" stroke="#2b2b29" stroke-width="1.5"><path d="M22 16.9v3a2 2 0 0 1-2.2 2 19.8 19.8 0 0 1-8.6-3.1 19.5 19.5 0 0 1-6-6A19.8 19.8 0 0 1 2.1 4.2 2 2 0 0 1 4.1 2h3a2 2 0 0 1 2 1.7c.1 1 .4 1.9.7 2.8a2 2 0 0 1-.5 2.1L8 9.9a16 16 0 0 0 6 6l1.3-1.3a2 2 0 0 1 2.1-.4c.9.3 1.8.6 2.8.7a2 2 0 0 1 1.7 2z"/></svg>
  <div class="contact-item" style="left:683px;"><h4>Phone</h4>+1 555-014-2290</div>

  <svg class="contact-icon" style="left:898px;" width="20" height="20" viewBox="0 0 20 20" fill="none" stroke="#2b2b29" stroke-width="2"><circle cx="10" cy="10" r="8"/><path d="M10 5v5H7"/></svg>
  <div class="contact-item" style="left:932px;"><h4>Hours</h4>Mon to Fri: 8am - 4pm<br>Sat &amp; Sun: By appointment</div>

  <div class="footer-rule" style="top:298px;"></div>
  <p class="copyright">2024 Roomora. All rights reserved</p>
</footer>

</body>
</html>
```